Website design for labour force (commercial truck driver) company

Looking for a Wordpress template (or design files in conjunction with a free Wordpress template).
Company tag line:
Tenvora – On Demand, Professional Drivers
Real Drivers | Real Standards | Real Results
Logo design has already been completed and is attached

Company provides contract drivers to trucking companies. Target market is both the trucking companies looking for drivers and drivers looking for work.
Design to encompass header / footer and basic page design, navigation menu, home page, contact page. Customer will add content and additional pages over time.

```html
<!DOCTYPE html>
<html lang="en">
<head>
<meta charset="utf-8">
<title>Tenvora – On Demand, Professional Drivers</title>
<link rel="stylesheet" href="https://fonts.googleapis.com/css2?family=Poppins:ital,wght@0,300;0,400;0,500;0,600;0,700;0,800;1,400&display=swap">
<style>
:root{
  --green:#138a69;
  --green-bright:#1fb88a;
  --dark:#231f20;
  --ink:#1f1c1d;
  --muted:#5a5a5a;
  --soft:#eeeeee;
  --line:#9a9a9a;
  --white:#ffffff;
  --mint:#d4ebe8;
}
*{box-sizing:border-box;margin:0;padding:0}
html,body{width:1200px;height:4762px;overflow:hidden}
body{font-family:"Poppins",sans-serif;color:var(--ink);background:var(--white)}
.page{position:relative;width:1200px;height:4762px;overflow:hidden}
.abs{position:absolute}
.backdrop{position:absolute;left:0;top:0}
.eyebrow{font-size:11px;font-weight:600;letter-spacing:3px;text-transform:uppercase;color:var(--green)}
.h-section{font-size:46px;line-height:54px;font-weight:300}
.h-section b{font-weight:800}
.btn{position:absolute;display:flex;align-items:center;height:48px;border-radius:24px;background:var(--green);color:var(--white);font-size:12px;font-weight:600;letter-spacing:2px;text-transform:uppercase;padding-left:64px}
.btn::before{content:"";position:absolute;left:12px;top:12px;width:24px;height:24px;border-radius:50%;background:var(--dark)}
.more{font-size:11px;font-weight:700;letter-spacing:2px;color:var(--green);text-transform:uppercase}
.photo{position:absolute;background:linear-gradient(135deg,#6b7a86,#c9b6a0)}

/* top bar */
.topbar-phone{left:85px;top:14px;color:var(--white);font-size:13px;font-weight:600;display:flex;align-items:center;gap:10px}
.topbar-follow{right:85px;top:15px;display:flex;align-items:center;gap:12px;color:var(--white);font-size:10px;font-weight:600;letter-spacing:3px}
.social{display:flex;gap:12px}
.social span{width:12px;height:12px;border-radius:50%;background:var(--white)}

/* header */
.brand{display:flex;align-items:center;gap:12px;font-weight:700;font-size:36px;letter-spacing:-.5px}
.brand i{display:block;width:52px;height:52px;border-radius:50%;background:var(--green)}
.nav{left:471px;top:97px;display:flex;gap:48px;font-size:12.5px;font-weight:600;letter-spacing:2px}
.nav .active{color:var(--green)}

/* hero */
.hero-eyebrow{left:85px;top:289px;font-size:10.5px;letter-spacing:2px}
.hero-title{left:85px;top:300px;font-size:66px;line-height:66px;font-weight:300}
.hero-title b{display:block;font-weight:800}
.hero-media{left:452px;top:148px;width:694px;height:508px;border-radius:70px 254px 254px 70px;background:linear-gradient(120deg,#c7d3d9 0%,#8d9aa3 40%,#8b6a4a 75%,#5d4a3b 100%)}
.hero-pill{border-radius:26px;background:#c8ccd0}
.slider-num{left:85px;top:606px;font-size:48px;font-weight:700;color:var(--green)}
.slider-total{left:294px;top:644px;font-size:12px;font-weight:700;color:var(--green)}

/* quote form */
.quote{left:85px;top:832px;width:313px;height:449px;background:var(--soft)}
.quote-head{height:50px;background:var(--green);color:var(--white);font-size:19px;letter-spacing:2.5px;display:flex;align-items:center;justify-content:center}
.quote-head b{margin-left:7px}
.field{position:absolute;left:25px;width:250px;border-bottom:1px solid var(--line);padding-bottom:6px;font-size:13.5px;display:flex;align-items:center;gap:8px;color:#333}
.field svg{width:12px;height:12px}
.quote-media{left:379px;top:869px;width:379px;height:407px;border-radius:40px 120px 18px 18px;background:linear-gradient(150deg,#7d2a22 0%,#c53a2c 45%,#3a3a3a 80%,#6b6b6b 100%)}

/* about */
.about{left:780px;top:880px;width:340px}
.about h2{font-size:48px;line-height:54px;font-weight:300;margin-top:8px}
.about h2 b{display:block;font-weight:800}
.about p{margin-top:14px;font-size:14px;line-height:25px;color:var(--muted)}

/* services */
.services-head{left:0;top:1470px;width:1200px;text-align:center;color:var(--white)}
.services-head .h-section{margin-top:4px}
.service{top:1596px;width:300px;color:var(--white)}
.service svg{width:64px;height:64px}
.service h3{margin-top:18px;font-size:17.5px;font-weight:700;letter-spacing:3.5px}
.service p{margin-top:8px;font-size:14px;line-height:25px;color:#cfcfcf}
.service .more{display:block;margin-top:10px}
.divider{top:1600px;width:1px;height:180px;background:#3d393a}

/* testimonials */
.testi-head{left:85px;top:2022px}
.testi-head .h-section{margin-top:4px}
.arrows{position:absolute;width:120px;height:54px;border:1.5px solid var(--green);border-radius:27px;display:flex;align-items:center;justify-content:space-around;color:var(--green);font-size:20px}
.arrows span.sep{width:1px;height:16px;background:currentColor}
.card{position:absolute;top:2176px;width:313px;height:296px;background:var(--soft);padding:34px 28px 0}
.card.featured{height:331px;background:var(--green);color:var(--white)}
.card svg{width:48px;height:34px}
.card p{margin-top:14px;font-size:14px;line-height:27.5px;color:#6a6a6a}
.card.featured p{color:var(--white)}
.client{display:flex;align-items:center;gap:14px;margin-top:22px}
.client i{width:46px;height:46px;border-radius:50%;background:linear-gradient(135deg,#cfd6dc,#8f9aa3);border:2px solid var(--white)}
.client b{display:block;font-size:14.5px;font-weight:700}
.client em{font-size:11px}

/* careers */
.careers-head{left:85px;top:2695px;color:var(--white)}
.careers-head .eyebrow{color:var(--white)}
.careers-head .h-section{margin-top:4px}
.job{position:absolute;width:507px;height:222px}
.job-card{position:absolute;left:0;top:0;width:400px;height:222px;background:var(--white);border-radius:111px 40px 40px 111px}
.job-photo{position:absolute;left:4px;top:30px;width:162px;height:162px;border-radius:50%;background:linear-gradient(135deg,#4d6e8f,#c9a27f)}
.job-accent{position:absolute;right:0;top:46px;width:130px;height:130px;border-radius:65px;background:var(--green-bright)}
.job-text{position:absolute;left:174px;top:60px;width:200px}
.job-text small{display:block;font-size:9.5px;font-weight:600;letter-spacing:2px}
.job-text h3{font-size:17px;font-weight:700;letter-spacing:2px;line-height:22px}
.job-text p{font-size:13.5px;line-height:25px;color:var(--muted);margin-top:3px}
.job-text .more{display:block;margin-top:10px}

/* blog */
.blog-head{left:0;top:3525px;width:1200px;text-align:center}
.blog-head .h-section{margin-top:4px}
.post{position:absolute;top:3628px;width:313px}
.post-media{position:relative;height:334px;background:linear-gradient(160deg,#2a4a8a,#1a1f2e 55%,#8a7767)}
.post.tall .post-media{height:384px;background:linear-gradient(160deg,#e8e8e8,#c9c9c9 40%,#4f5a46)}
.post.warm .post-media{background:linear-gradient(160deg,#9aa3a8,#5a534d 50%,#c8a58a)}
.date{position:absolute;right:18px;top:24px;height:30px;padding:0 14px;border-radius:15px;background:var(--green);color:var(--white);font-size:10.5px;font-weight:700;display:flex;align-items:center}
.post h3{margin-top:22px;font-size:17.5px;font-weight:600}
.post p{margin-top:8px;font-size:14px;line-height:27px;color:var(--muted)}
.post .more{display:block;margin-top:14px}

/* footer */
.footer-brand{left:85px;top:4400px;color:var(--white);font-size:32px}
.footer-brand i{width:48px;height:48px}
.footer-tag{left:391px;top:4396px;font-size:29px;line-height:36px;font-weight:700;color:var(--white)}
.footer-tag span{display:block;color:transparent;-webkit-text-stroke:1px var(--white)}
.footer-col{top:4536px;color:var(--white)}
.footer-col h4{font-size:15px;font-weight:700}
.footer-col p{margin-top:12px;font-size:12.5px;line-height:22px;color:#cfcfcf;display:flex;gap:8px}
.footer-col svg{flex:none;margin-top:5px}
.footer-follow{left:877px;top:4550px;display:flex;align-items:center;gap:14px;color:var(--white);font-size:10.5px;font-weight:600;letter-spacing:3px}
.footer-follow .rule{width:28px;height:1px;background:var(--white)}
.copyright{left:85px;top:4680px;font-size:12.5px;color:#cfcfcf}
.copyright span{color:var(--green-bright)}
.to-top{left:1051px;top:4658px;width:60px;height:60px;border-radius:50%;border:2px solid var(--green);background:var(--white);display:flex;align-items:center;justify-content:center}
</style>
</head>
<body>
<div class="page">

  <svg class="backdrop" width="1200" height="4762" viewBox="0 0 1200 4762" aria-hidden="true">
    <defs>
      <linearGradient id="heroSky" x1="0" y1="0" x2="0" y2="1">
        <stop offset="0" stop-color="#cfe8e5"/>
        <stop offset=".7" stop-color="#eef6f5"/>
        <stop offset="1" stop-color="#ffffff"/>
      </linearGradient>
    </defs>
    <rect x="0" y="46" width="1200" height="700" fill="url(#heroSky)"/>
    <rect x="0" y="0" width="1200" height="46" fill="#231f20"/>
    <path d="M0,1328 C400,1350 850,1330 1200,1230 L1200,1849 C1000,1960 800,1995 600,1985 C350,1970 150,1880 0,1784 Z" fill="#231f20"/>
    <path d="M0,2459 C250,2590 600,2650 1200,2644 L1200,3180 C900,3290 450,3390 0,3384 Z" fill="#138a69"/>
    <path d="M0,3384 C450,3390 900,3290 1200,3180 L1200,3515 C900,3420 450,3385 0,3384 Z" fill="#231f20"/>
    <path d="M0,4100 C300,4200 800,4290 1200,4310 L1200,4762 L0,4762 Z" fill="#231f20"/>
    <path d="M1200,4550 C1100,4600 1030,4690 1005,4762 L1200,4762 Z" fill="#138a69"/>
  </svg>

  <!-- top bar -->
  <div class="abs topbar-phone">
    <svg width="14" height="14" viewBox="0 0 24 24"><path d="M6.6 10.8a15 15 0 0 0 6.6 6.6l2.2-2.2c.3-.3.7-.4 1-.2 1.1.4 2.3.6 3.6.6.6 0 1 .4 1 1V20c0 .6-.4 1-1 1A17 17 0 0 1 3 4c0-.6.4-1 1-1h3.5c.6 0 1 .4 1 1 0 1.3.2 2.5.6 3.6.1.3 0 .7-.2 1z" fill="#1fb88a"/></svg>
    1800-555-019
  </div>
  <div class="abs topbar-follow">FOLLOW US
    <div class="social" aria-label="Social links"><span></span><span></span><span></span><span></span></div>
  </div>

  <!-- header -->
  <div class="abs brand" style="left:85px;top:79px"><i></i>Tenvora</div>
  <nav class="abs nav"><span class="active">HOME</span><span>ABOUT US</span><span>SERVICES</span><span>BLOG</span></nav>
  <div class="btn" style="left:897px;top:81px;width:218px">Contact Us ↗</div>

  <!-- hero -->
  <div class="abs hero-pill" style="left:395px;top:148px;width:420px;height:50px"></div>
  <div class="abs hero-pill" style="left:445px;top:240px;width:48px;height:48px"></div>
  <div class="abs hero-media" role="img" aria-label="Truck driver in a safety vest standing beside a white semi truck on a rural road"></div>
  <p class="abs eyebrow hero-eyebrow">Provides Contract Drivers To</p>
  <h1 class="abs hero-title" style="top:306px">Trucking<b>Companies</b></h1>
  <div class="btn" style="left:74px;top:470px;width:213px">Know More ↗</div>
  <div class="abs slider-num">01</div>
  <svg class="abs" style="left:140px;top:650px" width="146" height="6" aria-hidden="true"><rect x="0" y="2" width="146" height="1" fill="#138a69"/><rect x="0" y="1" width="36" height="3" fill="#138a69"/></svg>
  <div class="abs slider-total">04</div>

  <!-- request a quote -->
  <div class="abs quote">
    <div class="quote-head">REQUEST <b>A QUOTE</b></div>
    <div class="field" style="top:98px"><svg viewBox="0 0 24 24"><circle cx="12" cy="7" r="5" fill="#231f20"/><path d="M2 23c0-6 4-9 10-9s10 3 10 9z" fill="#231f20"/></svg>Name</div>
    <div class="field" style="top:158px"><svg viewBox="0 0 24 24"><rect x="1" y="4" width="22" height="16" rx="2" fill="#231f20"/><path d="M2 5l10 8 10-8" stroke="#eee" stroke-width="2" fill="none"/></svg>Email</div>
    <div class="field" style="top:218px"><svg viewBox="0 0 24 24"><path d="M6.6 10.8a15 15 0 0 0 6.6 6.6l2.2-2.2c.3-.3.7-.4 1-.2 1.1.4 2.3.6 3.6.6.6 0 1 .4 1 1V20c0 .6-.4 1-1 1A17 17 0 0 1 3 4c0-.6.4-1 1-1h3.5c.6 0 1 .4 1 1 0 1.3.2 2.5.6 3.6.1.3 0 .7-.2 1z" fill="#231f20"/></svg>Phone</div>
    <div class="field" style="top:276px"><svg viewBox="0 0 24 24"><path d="M12 1a8 8 0 0 0-8 8c0 6 8 14 8 14s8-8 8-14a8 8 0 0 0-8-8zm0 11a3 3 0 1 1 0-6 3 3 0 0 1 0 6z" fill="#231f20"/></svg>Location</div>
    <div class="btn" style="left:11px;top:340px;width:289px">Request A Quote</div>
  </div>
  <div class="abs quote-media" role="img" aria-label="Driver with a clipboard standing in front of a red semi truck cab"></div>

  <!-- about -->
  <div class="abs about">
    <p class="eyebrow" style="font-size:10.5px">About</p>
    <h2><b>Tenvora</b>Limited</h2>
    <p>Lorem ipsum dolor sit amet, cons adipng elit. Suspendisse blandit odio tortor, eu ege tortor scelerisque id. Phasellus a laoreet ipsum. Praesent vehula ac nisi in suscipit.</p>
  </div>
  <div class="btn" style="left:780px;top:1141px;width:196px">Read More ↗</div>

  <!-- services -->
  <div class="abs services-head">
    <p class="eyebrow" style="font-size:10.5px">Services</p>
    <h2 class="h-section"><b>What</b>&nbsp; We Offer</h2>
  </div>
  <div class="abs service" style="left:111px">
    <svg viewBox="0 0 64 64" aria-hidden="true"><circle cx="40" cy="20" r="16" fill="#138a69" opacity=".35"/><rect x="8" y="22" width="26" height="24" rx="3" fill="none" stroke="#1fb88a" stroke-width="2.5"/><path d="M34 30h10l6 8v8H34" fill="none" stroke="#1fb88a" stroke-width="2.5"/><circle cx="16" cy="50" r="4" fill="none" stroke="#1fb88a" stroke-width="2.5"/><circle cx="42" cy="50" r="4" fill="none" stroke="#1fb88a" stroke-width="2.5"/></svg>
    <h3>DRIVER SUPPLY</h3>
    <p>Vivamus rutrum ante eget auctor vestin ac tincidunt ligula.</p>
    <span class="more">More ↗</span>
  </div>
  <div class="abs divider" style="left:422px"></div>
  <div class="abs service" style="left:486px">
    <svg viewBox="0 0 64 64" aria-hidden="true"><circle cx="40" cy="20" r="16" fill="#138a69" opacity=".35"/><circle cx="30" cy="22" r="10" fill="none" stroke="#1fb88a" stroke-width="2.5"/><path d="M10 56c0-12 9-18 20-18s20 6 20 18" fill="none" stroke="#1fb88a" stroke-width="2.5"/><path d="M20 16h20" stroke="#1fb88a" stroke-width="2.5"/></svg>
    <h3>EXPERIENCE DRIVER</h3>
    <p>Vivamus rutrum ante eget auctor vestin ac tincidunt ligula.</p>
    <span class="more">More ↗</span>
  </div>
  <div class="abs divider" style="left:791px"></div>
  <div class="abs service" style="left:862px">
    <svg viewBox="0 0 64 64" aria-hidden="true"><circle cx="42" cy="18" r="14" fill="#138a69" opacity=".35"/><path d="M30 6l20 7v15c0 14-9 24-20 30C19 52 10 42 10 28V13z" fill="none" stroke="#1fb88a" stroke-width="2.5"/><path d="M22 32l6 6 12-13" fill="none" stroke="#1fb88a" stroke-width="2.5"/></svg>
    <h3>DRIVER SAFTY</h3>
    <p>Vivamus rutrum ante eget auctor vestin ac tincidunt ligula.</p>
    <span class="more">More ↗</span>
  </div>

  <!-- testimonials -->
  <div class="abs testi-head">
    <p class="eyebrow" style="font-size:10.5px">Testimonials</p>
    <h2 class="h-section"><b>What Our Happy</b><br>Clients Say</h2>
  </div>
  <div class="arrows" style="left:995px;top:2067px"><span>←</span><span class="sep"></span><span>→</span></div>

  <div class="card" style="left:85px">
    <svg viewBox="0 0 48 34" aria-hidden="true"><path d="M4 2h14l-6 30H4z M28 2h14l-6 30h-8z" fill="none" stroke="#138a69" stroke-width="2"/></svg>
    <p>Lorem ipsum dolor sit amet, cons adipng elit. Suspendisse blandit odio tortor, eu ege toor scelerisque id. Phasellus a laoreet ipsu.</p>
    <div class="client"><i role="img" aria-label="Client portrait"></i><div><b>Daniel R. Ashford</b><em>Client</em></div></div>
  </div>
  <div class="card featured" style="left:444px">
    <svg viewBox="0 0 48 34" aria-hidden="true"><path d="M4 2h14l-6 30H4z M28 2h14l-6 30h-8z" fill="none" stroke="#ffffff" stroke-width="2"/></svg>
    <p>Lorem ipsum dolor sit amet, cons adipng elit. Suspendisse blandit odio tortor, eu ege toor scelerisque id. Phasellus a laoreet ipsu. Donec sed felis tempu iaculis lorem</p>
    <div class="client"><i role="img" aria-label="Client portrait"></i><div><b>Clara M. Wells</b><em>Client</em></div></div>
  </div>
  <div class="card" style="left:801px">
    <svg viewBox="0 0 48 34" aria-hidden="true"><path d="M4 2h14l-6 30H4z M28 2h14l-6 30h-8z" fill="none" stroke="#138a69" stroke-width="2"/></svg>
    <p>Lorem ipsum dolor sit amet, cons adipng elit. Suspendisse blandit odio tortor, eu ege toor scelerisque id. Phasellus a laoreet ipsu.</p>
    <div class="client"><i role="img" aria-label="Client portrait"></i><div><b>Owen T. Rhodes</b><em>Client</em></div></div>
  </div>

  <!-- careers -->
  <div class="abs careers-head">
    <p class="eyebrow" style="font-size:10.5px">Careers</p>
    <h2 class="h-section"><b>The best place to</b><br>Work, Period</h2>
  </div>
  <div class="arrows" style="left:995px;top:2760px;border-color:#fff;color:#fff"><span style="opacity:.6">←</span><span class="sep"></span><span>→</span></div>

  <div class="job" style="left:85px;top:2847px">
    <div class="job-accent"></div>
    <div class="job-card"></div>
    <div class="job-photo" role="img" aria-label="Smiling truck driver in a plaid shirt at the cab door"></div>
    <div class="job-text"><small>PROFESSIONAL</small><h3>TRUCK DRIVER</h3><p>Vivamus rutrum ante eget auctor vestin ac</p><span class="more">Find Jobs ↗</span></div>
  </div>
  <div class="job" style="left:612px;top:2847px">
    <div class="job-accent"></div>
    <div class="job-card"></div>
    <div class="job-photo" role="img" aria-label="Driver in a high-visibility vest beside a blue truck"></div>
    <div class="job-text"><small>PROFESSIONAL</small><h3>TRUCK DRIVER</h3><p>Vivamus rutrum ante eget auctor vestin ac</p><span class="more">Find Jobs ↗</span></div>
  </div>
  <div class="job" style="left:85px;top:3102px">
    <div class="job-accent"></div>
    <div class="job-card"></div>
    <div class="job-photo" role="img" aria-label="Truck driver with arms crossed in front of a white truck"></div>
    <div class="job-text"><small>PROFESSIONAL</small><h3>TRUCK DRIVER</h3><p>Vivamus rutrum ante eget auctor vestin ac</p><span class="more">Find Jobs ↗</span></div>
  </div>
  <div class="job" style="left:612px;top:3102px">
    <div class="job-accent"></div>
    <div class="job-card"></div>
    <div class="job-photo" role="img" aria-label="Driver in a cap leaning on a truck window"></div>
    <div class="job-text"><small>PROFESSIONAL</small><h3>TRUCK DRIVER</h3><p>Vivamus rutrum ante eget auctor vestin ac</p><span class="more">Find Jobs ↗</span></div>
  </div>

  <!-- blog -->
  <div class="abs blog-head">
    <p class="eyebrow" style="font-size:10.5px">Our Blog</p>
    <h2 class="h-section"><b>Recent Blog</b> &amp; Articles</h2>
  </div>
  <article class="post" style="left:85px">
    <div class="post-media" role="img" aria-label="Driver climbing out of a blue truck cab at dusk"><span class="date">01 MAY</span></div>
    <h3>Nulla vitae nisi vehicula ertricies</h3>
    <p>Nulla vitae nisi vehicula eros ulies molestie non tempus nisl elementum facilisis</p>
    <span class="more">Read More ↗</span>
  </article>
  <article class="post tall" style="left:444px">
    <div class="post-media" role="img" aria-label="Woman with arms crossed standing in front of a white truck"><span class="date">05 JUNE</span></div>
    <h3>Nulla vitae nisi vehicula ertricies</h3>
    <p>Nulla vitae nisi vehicula eros ulies molestie non tempus nisl elementum facilisis</p>
    <span class="more">Read More ↗</span>
  </article>
  <article class="post warm" style="left:801px">
    <div class="post-media" role="img" aria-label="Smiling driver holding the steering wheel inside a truck cab"><span class="date">08 JULY</span></div>
    <h3>Nulla vitae nisi vehicula ertricies</h3>
    <p>Nulla vitae nisi vehicula eros ulies molestie non tempus nisl elementum facilisis</p>
    <span class="more">Read More ↗</span>
  </article>
  <div class="btn" style="left:475px;top:4199px;width:206px">View All ↗</div>

  <!-- footer -->
  <div class="abs brand footer-brand"><i></i>Tenvora</div>
  <p class="abs footer-tag">Company provides Contract Drivers<span>to Trucking Companies</span></p>
  <div class="abs footer-col" style="left:397px;width:200px">
    <h4>Contact Us</h4>
    <p><svg width="10" height="12" viewBox="0 0 24 24"><path d="M12 1a8 8 0 0 0-8 8c0 6 8 14 8 14s8-8 8-14a8 8 0 0 0-8-8zm0 11a3 3 0 1 1 0-6 3 3 0 0 1 0 6z" fill="#1fb88a"/></svg><span>12 Harbor Lane, Sydney, Australia</span></p>
  </div>
  <div class="abs footer-col" style="left:628px;width:230px">
    <h4>Get In Touch</h4>
    <p><svg width="11" height="11" viewBox="0 0 24 24"><path d="M6.6 10.8a15 15 0 0 0 6.6 6.6l2.2-2.2c.3-.3.7-.4 1-.2 1.1.4 2.3.6 3.6.6.6 0 1 .4 1 1V20c0 .6-.4 1-1 1A17 17 0 0 1 3 4c0-.6.4-1 1-1h3.5c.6 0 1 .4 1 1 0 1.3.2 2.5.6 3.6.1.3 0 .7-.2 1z" fill="#1fb88a"/></svg>1800-555-019</p>
    <p style="margin-top:6px"><svg width="11" height="11" viewBox="0 0 24 24"><rect x="1" y="4" width="22" height="16" rx="2" fill="#1fb88a"/></svg>info@tenvoralimited.com</p>
  </div>
  <div class="abs footer-follow">FOLLOW US <span class="rule"></span>
    <div class="social" aria-label="Social links"><span></span><span></span><span></span><span></span></div>
  </div>
  <p class="abs copyright">© 2025 <span>Tenvora Limited.</span> All right reserved</p>
  <div class="abs to-top" aria-label="Back to top">
    <svg width="22" height="30" viewBox="0 0 22 30"><path d="M11 28V3M3 11l8-8 8 8" fill="none" stroke="#138a69" stroke-width="2"/></svg>
  </div>
</div>
</body>
</html>
```